Home Building company needs lettering for our truck doors.

We need lettering for our truck doors and tailgate. We are a home building company in the construction industry. The trucks are gray in color and our company colors are dark blue, gray and white. We'd like the following included in the lettering; Our company name is; Brelvane Construction Company. My name is Dennis T. Brelvane, Builder/Carpenter/Cabinetmaker. Our phone numbers are; 781-555-0137 and 603-555-0192

Industry/Entity Type

Construction

Font styles to use
Other font styles liked:
• Times New Roman

```html
<!DOCTYPE html>
<html lang="en">
<head>
<meta charset="utf-8">
<title>Brelvane Construction Company – Door Lettering</title>
<link rel="stylesheet" href="https://fonts.googleapis.com/css2?family=Tinos:ital,wght@0,400;0,700;1,400&display=swap">
<style>
  :root {
    --navy: #10296b;
    --canvas: #ffffff;
  }
  * { margin: 0; padding: 0; box-sizing: border-box; }
  html, body {
    width: 1200px;
    height: 900px;
    overflow: hidden;
    background: var(--canvas);
  }
  .door-lettering {
    position: relative;
    width: 1200px;
    height: 900px;
    font-family: "Tinos", "Times New Roman", serif;
    color: var(--navy);
  }
  .door-lettering > * {
    position: absolute;
    line-height: 1;
    white-space: nowrap;
  }
  .company-name {
    left: 160px;
    top: 150px;
    font-size: 124px;
    font-weight: 700;
  }
  .company-suffix {
    right: 160px;
    top: 276px;
    font-size: 60px;
    font-weight: 700;
  }
  .owner-name {
    right: 176px;
    top: 410px;
    font-size: 64px;
    font-style: italic;
    font-weight: 400;
  }
  .owner-trades {
    right: 168px;
    top: 506px;
    font-size: 40px;
    font-weight: 400;
  }
  .phone-numbers {
    left: 184px;
    top: 668px;
    font-size: 64px;
    font-weight: 700;
  }
</style>
</head>
<body>
  <main class="door-lettering">
    <h1 class="company-name">Brelvane</h1>
    <p class="company-suffix">Construction Company</p>
    <p class="owner-name">Dennis T. Brelvane</p>
    <p class="owner-trades">Builder/Carpenter/Cabinetmaker</p>
    <p class="phone-numbers">781-555-0137 | 603-555-0192</p>
  </main>
</body>
</html>
```